Stonefield Partners - Web Design

I have recently established a business called Stonefield Partners. The business is focused on providing property developers with project financing solutions. This is not a real estate website so please do not provide such pics or design. I provide financial solutions.

I have been in the financial markets for the past 20 years covering all asset classes from trading through to portfolio management, structuring and business development. The majority of this time was spent with building new business and expanding into new opportunities.

This is a start-up business so there isn't much content at this stage. Therefore, its all about first impressions. I want a design that portray confidence; and that I can deliver a workable solution. It must provide the perception of sophistication, innovation, yet simplistic so its not trying to deceive/hide something. Most importantly it must give the Client a sense of trust and reliability.

I would like to have the website portray my depth of experience in providing financing solutions and consultancy services in achieving the investment objectives. However, I would like to avoid looking like a one man band. I do have access to resources just not directly employed by the company.

Anyway, I hope this is enough to at least wet your appetite. I recently had a logo created on ArtHive that should set the theme/style of the website

Project Deadline Extended
Reason: Increase time to allow web designer/developer more time to understand the style I am after.

All, Thank you for your current designs. I am based in Singapore, however, I am currently traveling today but will respond by later tonight or tomorrow. Rolf

All, A general observation. Please do not include photos of houses, architectural drawings or images that portal construction or real estate. This implies I am either a property agent or in some way directly involve in selling property...very misleading. Remember, I am involved in provide financial solutions not selling property. Rolf

All, Please avoid using numerous people within the site as it may represent that my business has a large number of staff when in fact its only me. However, I also don't want to look like a "one man band". So be balanced on using people - I am not sure I want people at all. Thanks Rolf

Some designers are not reading the brief or previous messages. If you do more then once I will simply not comment and eliminate ask not to provide any more.

please stop using pictures and/or logos that imply - I manage their money - I protect their money - I grow their money - I offer homes loans - that I do house calls with individuals (i.e no couples shaking heads with a guy) - no house pictures or symbols i.e. it looks like a property website - I have a large organisation (i.e. team of people) If any design include the above I will eliminate it REMEMBER: I am providing innovative financial solutions - NOT asset/fund manager, bank manager or real estate manager thank you

All Please be creative and innovative with your pics. Also ensure you have the rights to use the pics. I have seen basic stock photos being used and again have not read by brief or previous comments. For instance, they use the words "sustainable growth" in google and click on images and you will see most of the images being used. these will be eliminated instantly and not asked to return.

Please, if you use the name of the Company as a Label or Statement can please ensure it remains in the same style as the Logo, i.e. all Caps Large with small.

All, I have decided that I don't want to have people in the main pic on the front page so please provide other inspirational pics. Thanks

guys I found a coffee advert whilst in Vietnam. I like the colour selection and thought it would be inspirational.i ahve added it yo my bried f

```html
<!DOCTYPE html>
<html lang="en">
<head>
<meta charset="utf-8">
<title>Stonefield Partners</title>
<link href="https://fonts.googleapis.com/css2?family=Open+Sans:wght@400;600;700&family=Source+Sans+3:wght@400;600;700&display=swap" rel="stylesheet">
<style>
:root{
  --ink:#1a1a1a;
  --header:#161616;
  --footer:#121212;
  --footer-bar:#0b0b0b;
  --gold:#c9a230;
  --gold-soft:#d8b44a;
  --page:#ececec;
  --panel:#ffffff;
  --panel-alt:#f6f6f6;
  --text:#444444;
  --muted:#8a8a8a;
  --light:#e4e4e4;
  --icon:#9a9a9a;
}
*{margin:0;padding:0;box-sizing:border-box}
html,body{width:738px;height:1200px;overflow:hidden}
body{position:relative;background:var(--page);font-family:"Open Sans",sans-serif;color:var(--text);font-size:7px;line-height:1.5}
.abs{position:absolute}

/* header */
.site-header{left:0;top:0;width:738px;height:200px;background:radial-gradient(ellipse at 50% 0%,#2a2a2a 0%,var(--header) 70%)}
.brand{left:112px;top:24px;display:flex;align-items:center;gap:8px}
.brand-mark{width:22px;height:22px;background:var(--gold)}
.brand-name{font-family:"Source Sans 3",sans-serif;font-weight:600;font-size:15px;letter-spacing:1.5px;color:var(--gold-soft)}
.main-nav{top:0;left:0;width:738px;height:60px}
.main-nav a{position:absolute;top:36px;font-size:6px;font-weight:700;color:#fff;text-decoration:none;letter-spacing:.3px}
.main-nav a.active{top:30px;padding:6px 9px;background:var(--gold);color:var(--ink)}
.tagline{left:111px;top:74px;width:516px;text-align:center;font-family:"Source Sans 3",sans-serif;font-size:21px;line-height:26px;color:#cfcfcf}
.tagline b{color:#fff;font-weight:700}

/* hero */
.hero{left:111px;top:130px;width:516px;height:253px;background:linear-gradient(135deg,#5a6470 0%,#c7ccd3 40%,#e9ecef 60%,#9ba5b1 100%)}
.hero-title{left:148px;top:232px;padding:4px 8px;background:var(--ink);color:#fff;font-family:"Source Sans 3",sans-serif;font-weight:700;font-size:12px}
.hero-sub{left:148px;top:264px;padding:4px 8px;background:var(--gold);color:#3a2d05;font-family:"Source Sans 3",sans-serif;font-size:11px}

/* intro */
.intro{left:111px;top:383px;width:516px;height:129px;background:var(--panel);text-align:center}
.intro h1{margin-top:22px;font-family:"Source Sans 3",sans-serif;font-size:15px;font-weight:700;color:var(--ink)}
.intro .rule{width:36px;height:1px;background:var(--light);margin:8px auto 6px}
.intro p{width:470px;margin:0 auto;font-size:9px;line-height:13px;color:#a3a3a3}
.btn{display:inline-block;margin-top:8px;padding:4px 12px;background:var(--gold);color:var(--ink);font-size:6px;font-weight:700;text-decoration:none}

/* services */
.services{left:111px;top:522px;width:516px;height:220px;background:var(--panel)}
.section-title{font-family:"Source Sans 3",sans-serif;font-weight:700;font-size:11px;color:var(--ink)}
.services .section-title{position:absolute;left:23px;top:12px}
.services .lead{position:absolute;left:23px;top:30px;font-size:5.5px;color:var(--muted)}
.service{position:absolute;width:220px}
.service svg{position:absolute;left:0;top:0}
.service h3{margin-left:42px;font-family:"Source Sans 3",sans-serif;font-size:10px;font-weight:700;color:var(--gold)}
.service p{margin:8px 0 0 42px;font-size:5.5px;line-height:9px;color:var(--muted)}

/* posts band */
.band{left:111px;top:750px;width:516px;height:190px;background:var(--panel-alt)}
.band .col{position:absolute;top:14px;width:150px}
.band .section-title{font-size:10px;margin-bottom:12px}
.post{position:relative;height:58px}
.post .thumb{position:absolute;left:0;top:0;width:32px;height:26px;background:linear-gradient(135deg,#3e5a7a,#c9ced6)}
.post .date{position:absolute;left:0;top:30px;width:32px;padding:2px 0;background:var(--gold);color:var(--ink);font-size:5px;font-weight:700;text-align:center}
.post h4{margin-left:42px;font-size:6.5px;font-weight:700;color:var(--ink)}
.post p{margin:3px 0 0 42px;font-size:5.5px;line-height:8px;color:var(--muted)}
.why p{font-size:5.5px;line-height:8px;color:var(--muted)}
.why ul{list-style:none;margin-top:6px}
.why li{position:relative;padding-left:9px;font-size:5.5px;line-height:9px;color:var(--muted)}
.why li svg{position:absolute;left:0;top:2px}
.quote{background:#ebebeb;padding:8px 10px;font-size:5.5px;line-height:8px;color:var(--muted)}
.quote-by{text-align:right;font-size:5.5px;font-weight:700;color:var(--ink);margin:6px 0 10px}
.quote-by.left{text-align:left}

/* footer */
.site-footer{left:111px;top:948px;width:516px;height:219px;background:var(--footer)}
.site-footer .col{position:absolute;top:16px;width:110px}
.site-footer h5{font-family:"Source Sans 3",sans-serif;font-size:9px;font-weight:700;color:#fff;margin-bottom:12px}
.site-footer p{font-size:5.5px;line-height:8px;color:#cfcfcf}
.site-footer .meta{color:var(--gold);margin:4px 0 10px}
.contact-line{display:flex;align-items:center;gap:5px;font-size:5.5px;color:#cfcfcf;margin-top:4px}
.footer-bar{left:111px;top:1130px;width:516px;height:37px;background:var(--footer-bar)}
.copyright{position:absolute;left:23px;top:14px;font-size:6px;color:var(--gold)}
.social{position:absolute;right:22px;top:12px;display:flex;gap:5px}
.social span{width:12px;height:12px;border-radius:50%;background:#e6e6e6}
</style>
</head>
<body>

<header class="site-header abs">
  <div class="brand abs"><span class="brand-mark"></span><span class="brand-name">STONEFIELD PARTNERS</span></div>
  <nav class="main-nav abs">
    <a class="active" href="#" style="left:330px">HOME</a>
    <a href="#" style="left:390px">ABOUT</a>
    <a href="#" style="left:446px">PORTFOLIO</a>
    <a href="#" style="left:506px">SERVICE</a>
    <a href="#" style="left:557px">BLOG</a>
    <a href="#" style="left:605px">CONTACT</a>
  </nav>
  <p class="tagline abs">You build, we <b>finance - flexible</b>, affordable property development finance.</p>
</header>

<section class="hero abs" role="img" aria-label="Hands reviewing financial charts and a tablet on a desk"></section>
<div class="hero-title abs">Risus Dolor Fermentum Aenean Fusce</div>
<div class="hero-sub abs">Mollis Elit Egestas Euismod Bibendum</div>

<section class="intro abs">
  <h1>Financing Commercial Property Development made easy.</h1>
  <div class="rule"></div>
  <p>Cum sociis natoque penatibus et magnis dis parturient montes, nascetur ridiculus mus. Sed posuere consectetur est at lobortis. Maecenas sed diam eget risus varius blandit sit amet non magna.</p>
  <a class="btn" href="#">See All Prices</a>
</section>

<section class="services abs">
  <h2 class="section-title">What Do We Provide</h2>
  <p class="lead">Vestibulum id ligula porta felis euismod semper. Donec id elit non mi porta gravida at eget metus. Nullam id dolor id nibh ultricies vehicula ut id elit.</p>

  <div class="service" style="left:23px;top:60px">
    <svg width="30" height="22" viewBox="0 0 30 22"><rect x="1" y="5" width="20" height="15" fill="none" stroke="#9a9a9a" stroke-width="1.5"/><path d="M10 14 L27 2" stroke="#9a9a9a" stroke-width="2"/></svg>
    <h3>Property Advisory</h3>
    <p>Donec sed nisi mi porta gravida at eget metus. Cras justo odio, dapibus ac facilisis in, egestas eget quam. Vestibulum ligula porta felis cras ridiculus dapibus, aenean eu leo quam.</p>
  </div>
  <div class="service" style="left:267px;top:60px">
    <svg width="30" height="22" viewBox="0 0 30 22"><circle cx="9" cy="5" r="3.5" fill="#9a9a9a"/><circle cx="20" cy="5" r="3.5" fill="#9a9a9a"/><rect x="5" y="10" width="8" height="11" rx="2" fill="#9a9a9a"/><rect x="16" y="10" width="8" height="11" rx="2" fill="#9a9a9a"/></svg>
    <h3>Residential Body Corporate Finance</h3>
    <p>Fusce dapibus, tellus ac cursus commodo, tortor mauris condimentum nibh, ut fermentum massa justo sit amet risus. Donec id elit non mi.</p>
  </div>
  <div class="service" style="left:23px;top:140px">
    <svg width="30" height="22" viewBox="0 0 30 22"><rect x="2" y="6" width="24" height="15" rx="1" fill="#9a9a9a"/><rect x="10" y="2" width="8" height="5" fill="none" stroke="#9a9a9a" stroke-width="1.5"/></svg>
    <h3>Development Finance</h3>
    <p>Mollis est non commodo luctus, nisi erat porttitor ligula, eget lacinia odio sem nec elit. Aenean lacinia bibendum nulla consectetur. Integer posuere erat a ante venenatis dapibus.</p>
  </div>
  <div class="service" style="left:267px;top:140px">
    <svg width="30" height="22" viewBox="0 0 30 22"><path d="M2 18 L10 12 L18 14 L26 8 L26 12 L18 19 L8 19 Z" fill="#9a9a9a"/><circle cx="20" cy="6" r="4" fill="#9a9a9a"/></svg>
    <h3>Development and Project Management</h3>
    <p>Morbi leo risus, porta ac consectetur, vestibulum at eros. Praesent commodo cursus magna, vel scelerisque nisl consectetur. Aenean lacinia bibendum nulla sed consectetur.</p>
  </div>
</section>

<section class="band abs">
  <div class="col" style="left:23px;width:150px">
    <h2 class="section-title">Latest Posts</h2>
    <article class="post">
      <div class="thumb" role="img" aria-label="Blog post thumbnail of a business meeting"></div>
      <div class="date">21 JAN</div>
      <h4>Tortor Purus Mollis Quam</h4>
      <p>Praesent commodo cursus magna. Maecenas faucibus mollis interdum. Praesent commodo cursus magna.</p>
    </article>
    <article class="post">
      <div class="thumb" role="img" aria-label="Blog post thumbnail of a desk with documents"></div>
      <div class="date">15 JAN</div>
      <h4>Fringilla Venenatis Cursus</h4>
      <p>Etiam porta sem malesuada magna mollis euismod. Donec ullamcorper nulla non metus auctor fringilla.</p>
    </article>
  </div>
  <div class="col why" style="left:186px;width:150px">
    <h2 class="section-title">Why Choose Us</h2>
    <p>Duis mollis, est non commodo luctus, nisi porttitor ligula, eget lacinia odio sem nec elit. Aenean eu leo quam. Pellentesque ornare sem lacinia quam venenatis vestibulum. Aenean lacinia bibendum nulla sed consectetur. Nulla vitae elit libero, a pharetra augue.</p>
    <ul>
      <li><svg width="6" height="5" viewBox="0 0 6 5"><path d="M0.5 2.5 L2.3 4.3 L5.5 0.7" fill="none" stroke="#9a9a9a" stroke-width="1"/></svg>Donec ullamcorper nulla non metus auctor.</li>
      <li><svg width="6" height="5" viewBox="0 0 6 5"><path d="M0.5 2.5 L2.3 4.3 L5.5 0.7" fill="none" stroke="#9a9a9a" stroke-width="1"/></svg>Cras justo odio, dapibus ac facilisis in, egestas eget quam. Sed posuere consectetur.</li>
      <li><svg width="6" height="5" viewBox="0 0 6 5"><path d="M0.5 2.5 L2.3 4.3 L5.5 0.7" fill="none" stroke="#9a9a9a" stroke-width="1"/></svg>Praesent commodo cursus magna.</li>
      <li><svg width="6" height="5" viewBox="0 0 6 5"><path d="M0.5 2.5 L2.3 4.3 L5.5 0.7" fill="none" stroke="#9a9a9a" stroke-width="1"/></svg>Nullam id dolor id nibh ultricies vehicula ut.</li>
    </ul>
  </div>
  <div class="col" style="left:349px;width:145px">
    <h2 class="section-title">Testimonials</h2>
    <blockquote class="quote" style="margin-top:20px">Nullam quis risus eget urna mollis ornare vel eu leo. Maecenas faucibus mollis interdum. Nulla vitae elit libero, a pharetra augue.</blockquote>
    <p class="quote-by">by Dan Merrow</p>
    <blockquote class="quote">Fusce dapibus, tellus ac cursus commodo, tortor mauris condimentum nibh. Nulla vitae elit libero, a pharetra.</blockquote>
    <p class="quote-by left">by Mara Quint</p>
  </div>
</section>

<footer class="site-footer abs">
  <div class="col" style="left:23px">
    <h5>Popular Posts</h5>
    <p>Vivamus sagittis lacus vel augue metus laoreet rutrum dolor auctor.</p>
    <p class="meta">14 Nov, 2012</p>
    <p>Scelerisque nisl consectetur et.</p>
    <p class="meta">22 Nov, 2012</p>
    <p>Pellentesque ornare sem lacinia quam venenatis vestibulum.</p>
    <p class="meta">15 July, 2012</p>
  </div>
  <div class="col" style="left:143px">
    <h5>Updates</h5>
    <p>Praesent commodo cursus magna. Morbi leo risus nulla consectetur.</p>
    <p class="meta">21 hours ago</p>
    <p>Vestibulum id ligula porta euismod semper, auctor dolor fermentum.</p>
    <p class="meta">3 days ago</p>
    <p>Donec ullamcorper nulla non metus.</p>
    <p class="meta">3 days ago</p>
  </div>
  <div class="col" style="left:267px">
    <h5>A Little About Us</h5>
    <p>Lorem ipsum dolor sit amet, consectetur adipiscing elit. Duis mollis, est non commodo luctus, nisi erat porttitor ligula, eget lacinia odio sem nec elit. Duis mollis, est non commodo luctus, nisi erat porttitor.</p>
    <p style="margin-top:8px">Donec id elit non porta gravida at eget metus. Nullam quis risus eget urna mollis ornare.</p>
  </div>
  <div class="col" style="left:387px">
    <h5>Get in Touch</h5>
    <p>Fusce dapibus, tellus commodo, tortor mauris condimentum ultrices fermentum, porta sem. Aenean eu leo quam. Pellentesque ornare sem lacinia quam venenatis vestibulum.</p>
    <div class="contact-line" style="margin-top:8px"><svg width="6" height="8" viewBox="0 0 6 8"><path d="M3 0 A3 3 0 0 1 6 3 C6 5 3 8 3 8 C3 8 0 5 0 3 A3 3 0 0 1 3 0 Z" fill="#c9a230"/></svg><span>Harbour Lane No: 12/08<br>Eastport</span></div>
    <div class="contact-line"><svg width="6" height="7" viewBox="0 0 6 7"><rect x="1" y="0" width="4" height="7" rx="1" fill="#c9a230"/></svg><span>0200 318 44 90</span></div>
    <div class="contact-line"><svg width="7" height="5" viewBox="0 0 7 5"><rect width="7" height="5" fill="#c9a230"/><path d="M0 0 L3.5 3 L7 0" fill="none" stroke="#121212" stroke-width=".7"/></svg><span>hello@northpier.com</span></div>
  </div>
</footer>
<div class="footer-bar abs">
  <p class="copyright">© Stonefield Partners - All Rights Reserved.</p>
  <div class="social"><span></span><span></span><span></span><span></span><span></span><span></span><span></span></div>
</div>

</body>
</html>
```